Life Coach for Lawyers Business Card Design

Elegant, original, business card design for life coaching service for associate attorneys who work in big law and struggle with stress, overwhelm, and time management. Double sided design.

Target Market(s)

Women associate attorneys who work in big law and struggle with stress, overwhelm, and time management.

Industry/Entity Type

Life Coaching

Contact Information for Business Card

Marissa Pendrell
Life Coach
518.677.3941
calmbriefcounsel.net
marissa@calmbriefcounsel.net
@calmbriefcounsel (Instagram)

Font styles to use
Other font styles liked:
• Silver South font duo. See uploaded files.

Requirements
Must have
• Icons for phone, website, email, and Instagram instead of words. Specific colors used in my logo (171B2B, 421121, FFFFFF)
Nice to have
• Foil. Embossed. Feminine design.
Should not have
• Any colors other than those used in logo. See uploaded files.

```html
<!DOCTYPE html>
<html lang="en">
<head>
<meta charset="utf-8">
<title>Marissa Pendrell · Life Coach</title>
<link href="https://fonts.googleapis.com/css2?family=Great+Vibes&family=Josefin+Sans:wght@300;400&display=swap" rel="stylesheet">
<style>
  :root {
    --plum: #3a1824;
    --plum-soft: #5a3340;
    --ink: #171b2b;
    --white: #ffffff;
  }
  * { margin: 0; padding: 0; box-sizing: border-box; }
  html, body { width: 1019px; height: 1200px; overflow: hidden; background: var(--plum); }
  .card-sheet { position: relative; width: 1019px; height: 1200px; background: var(--plum); color: var(--white); }

  .floral-band {
    position: absolute; left: 0; top: 0; width: 1019px; height: 264px;
    background: linear-gradient(180deg, var(--plum-soft) 0%, var(--plum) 100%);
  }
  .floral-column {
    position: absolute; left: 0; top: 600px; width: 152px; height: 600px;
    background: linear-gradient(90deg, var(--plum-soft) 0%, var(--plum) 100%);
  }

  .name {
    position: absolute; font-family: "Great Vibes", cursive;
    font-size: 70px; line-height: 1; white-space: nowrap; font-weight: 400;
  }
  .role {
    position: absolute; font-family: "Josefin Sans", sans-serif;
    font-weight: 300; font-size: 33px; letter-spacing: 3px; line-height: 1; white-space: nowrap;
  }

  .front .name { left: 0; width: 1019px; text-align: center; top: 350px; }
  .front .role { left: 0; width: 1019px; text-align: center; top: 478px; }

  .back .name { right: 85px; top: 688px; }
  .back .role { right: 95px; top: 795px; }

  .contact-list { position: absolute; right: 90px; top: 905px; list-style: none; }
  .contact-item {
    display: flex; justify-content: flex-end; align-items: center; gap: 8px;
    height: 40px; margin-bottom: 21px;
    font-family: "Josefin Sans", sans-serif; font-weight: 300; font-size: 29px; white-space: nowrap;
  }
  .contact-item svg { flex: none; }
  .social-mark { width: 44px; height: 44px; border: 3px solid var(--white); border-radius: 10px; flex: none; }
</style>
</head>
<body>
<main class="card-sheet">
  <div class="floral-band" role="img" aria-label="White outlined daisy flowers along the top edge"></div>
  <div class="floral-column" role="img" aria-label="Column of small white outlined daisy flowers down the left edge"></div>

  <section class="front">
    <h1 class="name">Marissa Pendrell</h1>
    <p class="role">LIFE COACH</p>
  </section>

  <section class="back">
    <h2 class="name">Marissa Pendrell</h2>
    <p class="role">LIFE COACH</p>

    <ul class="contact-list">
      <li class="contact-item">
        <svg width="48" height="48" viewBox="0 0 48 48" aria-hidden="true">
          <circle cx="24" cy="24" r="21" fill="none" stroke="#fff" stroke-width="3"/>
          <path d="M17 13c2 0 3 4 3 5s-2 2-2 3c1 3 4 6 7 7 1 0 2-2 3-2s5 1 5 3-2 4-4 4c-8 0-15-7-15-15 0-2 1-5 3-5z" fill="#fff"/>
        </svg>
        <span>518.677.3941</span>
      </li>
      <li class="contact-item">
        <svg width="52" height="48" viewBox="0 0 52 48" aria-hidden="true">
          <circle cx="26" cy="24" r="21" fill="none" stroke="#fff" stroke-width="3"/>
          <ellipse cx="26" cy="24" rx="9" ry="21" fill="none" stroke="#fff" stroke-width="2.5"/>
          <rect x="2" y="17" width="48" height="14" rx="2" fill="#fff"/>
          <text x="26" y="28.5" text-anchor="middle" font-family="Josefin Sans, sans-serif" font-size="11" font-weight="400" fill="#3a1824">www</text>
        </svg>
        <span>calmbriefcounsel.net</span>
      </li>
      <li class="contact-item">
        <svg width="52" height="48" viewBox="0 0 52 48" aria-hidden="true">
          <path d="M4 22 L26 38 L48 22 V46 H4 Z" fill="none" stroke="#fff" stroke-width="3" stroke-linejoin="round"/>
          <text x="26" y="28" text-anchor="middle" font-family="Josefin Sans, sans-serif" font-size="30" font-weight="400" fill="#fff">@</text>
        </svg>
        <span>marissa@calmbriefcounsel.net</span>
      </li>
      <li class="contact-item">
        <span class="social-mark" aria-hidden="true"></span>
        <span>@calmbriefcounsel</span>
      </li>
    </ul>
  </section>
</main>
</body>
</html>
```